Update shopping site

Our current shopping website is outdated and we are wanting to update our shopping site to have a fresh new look/design.

Create a Web Design (Uncoded - PSD layout only)

We want you to develop the design for 4 pages:
1) Home Page
2) Remedy Type
3) Health Condition
4) Consultations

www.fernmoorwell.com

Reason: Close to choosing design and a few missing items to be resolved.

Industry/Entity Type

Shopping

```html
<!DOCTYPE html>
<html lang="en">
<head>
<meta charset="utf-8">
<title>Health Condition – Fernmoor Well</title>
<link rel="stylesheet" href="https://fonts.googleapis.com/css2?family=Merriweather:wght@400;700&family=Open+Sans:wght@400;600;700&display=swap">
<style>
:root{
  --green:#4a7c0c;
  --cream:#f5f3ee;
  --sand:#ece9df;
  --text:#222;
  --line:#e3e0d8;
  --star:#f2b01e;
}
*{box-sizing:border-box;margin:0;padding:0}
html,body{width:1200px;height:2305px;overflow:hidden}
body{position:relative;font-family:"Open Sans",Arial,sans-serif;color:var(--text);background:#fff}
a{color:inherit;text-decoration:none}
.abs{position:absolute}

/* wordmark */
.brand{position:absolute;display:flex;align-items:center;gap:12px;font-family:"Merriweather",Georgia,serif;font-weight:400;color:var(--green);white-space:nowrap}
.brand-dot{border-radius:50%;border:2px solid var(--green);flex:none}
.header-brand{left:161px;top:18px;font-size:18px}
.header-brand .brand-dot{width:38px;height:38px}
.footer-brand{left:161px;top:1974px;font-size:22px}
.footer-brand .brand-dot{width:52px;height:52px}

/* top bar */
.topbar{left:0;top:0;width:1200px;height:74px;background:var(--cream)}
.account-links{left:611px;top:28px;font-size:12px;font-weight:600;color:#555;display:flex;gap:16px}
.signin{left:790px;top:23px;width:70px;height:28px;border-radius:14px;background:var(--green);color:#fff;font-size:11px;font-weight:700;display:flex;align-items:center;justify-content:center}
.search{left:881px;top:24px;width:158px;height:27px;border:1px solid #d8d5cc;border-radius:14px;background:#fff;font-size:10px;color:#aaa;padding:6px 12px}
.search svg{position:absolute;right:10px;top:7px}

/* nav */
.navbar{left:0;top:74px;width:1200px;height:55px;background:var(--sand)}
.findus{left:161px;top:74px;width:112px;height:55px;background:var(--green);color:#fff;font-size:12px;font-weight:700;display:flex;align-items:center;justify-content:center;gap:12px}
.mainnav{left:410px;top:74px;height:55px;display:flex;gap:24px;align-items:center;font-size:12px;font-weight:600;color:#555}
.mainnav .active{color:var(--green);border-bottom:2px solid var(--green);padding:18px 0 16px}

/* hero */
.hero-photo{left:0;top:129px;width:1200px;height:524px;background:linear-gradient(100deg,#2f2a25 0%,#6b5c4e 35%,#8a7a68 55%,#3d3833 80%,#2a2a2d 100%)}
.hero-shade{left:0;top:129px;width:1200px;height:524px;background:linear-gradient(90deg,rgba(0,0,0,.45),rgba(0,0,0,.1) 60%,rgba(0,0,0,.3))}
.hero-title{left:161px;top:312px;font-family:"Merriweather",Georgia,serif;font-size:40px;font-weight:700;color:#fff}
.hero-text{left:161px;top:378px;width:420px;font-size:12px;line-height:21px;color:#fff}

/* sidebar */
.side-title{left:161px;top:802px;font-family:"Merriweather",Georgia,serif;font-size:16px;font-weight:700;color:var(--green)}
.side-list{left:172px;top:848px;list-style:none;font-size:12px;font-weight:600}
.side-list li{height:30px;line-height:18px;position:relative;padding-left:12px}
.side-list li::before{content:"›";position:absolute;left:0;top:-1px;font-size:13px}
.side-list li.on{color:var(--green)}

/* toolbar */
.toolbar{top:760px;font-size:11px;font-weight:700;letter-spacing:.3px}
.toolbar b{color:var(--green)}

/* products */
.card{width:171px;height:255px;border:1px solid var(--line);border-bottom:3px solid var(--green);text-align:center;background:#fff}
.card.sel{border:2px solid var(--green);border-bottom:3px solid var(--green)}
.thumb{height:154px;margin:0 15px;background:linear-gradient(#faf9f7,#f1efec)}
.thumb.photo-a{margin:16px 0 0;height:138px;background:linear-gradient(135deg,#d8d3cc,#6e4a3a 55%,#b9aa95)}
.thumb.photo-b{margin:16px 0 0;height:138px;background:linear-gradient(135deg,#e6e2dc,#7a5a3c 50%,#c9b98e)}
.name{font-family:"Merriweather",Georgia,serif;font-size:12px;font-weight:700;margin-top:14px}
.sel .name{color:var(--green)}
.desc{font-size:10px;color:#444;line-height:15px;margin-top:6px;padding:0 14px}
.star{left:571px;top:1104px}

/* pagination */
.pager{left:419px;top:1754px;display:flex;font-size:10px;color:#bbb;font-weight:600}
.pager span{width:30px;height:26px;display:flex;align-items:center;justify-content:center;border-bottom:2px solid var(--line)}
.pager .cur{color:var(--text);border-bottom-color:var(--green)}
.pager .next{width:61px;background:var(--green);color:#fff;font-weight:700;border:none}

/* footer */
.footer-band{left:0;top:1889px;width:1200px;height:377px;background:var(--cream);border-top:2px solid #d9d6cd}
.mission{left:161px;top:2042px;width:345px;font-size:11px;line-height:18px;color:#333}
.contact{left:161px;top:2104px;font-size:11px;line-height:22px;font-weight:600}
.contact span{color:var(--green)}
.fcol{top:1982px;font-size:11px;line-height:22.5px}
.fcol h4{font-size:11px;font-weight:700;letter-spacing:.3px;margin-bottom:10px}
.totop{left:1118px;top:2194px;width:27px;height:27px;background:#ebe8df;display:flex;align-items:center;justify-content:center}
.bottombar{left:0;top:2266px;width:1200px;height:39px;background:var(--sand);font-size:10px;color:#555;font-weight:600}
.bottombar .l{position:absolute;left:161px;top:13px}
.bottombar .r{position:absolute;right:161px;top:13px}
</style>
</head>
<body>

<header>
  <div class="abs topbar"></div>
  <a class="brand header-brand" href="#"><span class="brand-dot"></span><span>Fernmoor Well</span></a>
  <nav class="abs account-links"><a href="#">My account</a><a href="#">Shopping cart</a></nav>
  <a class="abs signin" href="#">Sign in</a>
  <div class="abs search">Search...
    <svg width="10" height="10" viewBox="0 0 10 10"><circle cx="4" cy="4" r="3" fill="none" stroke="#aaa" stroke-width="1.3"/><path d="M6.3 6.3 9 9" stroke="#aaa" stroke-width="1.3"/></svg>
  </div>

  <div class="abs navbar"></div>
  <a class="abs findus" href="#">Find us
    <svg width="12" height="16" viewBox="0 0 12 16"><path d="M6 1a5 5 0 0 1 5 5c0 4-5 9-5 9S1 10 1 6a5 5 0 0 1 5-5z" fill="none" stroke="#fff" stroke-width="1.4"/><circle cx="6" cy="6" r="1.8" fill="none" stroke="#fff" stroke-width="1.3"/></svg>
  </a>
  <nav class="abs mainnav">
    <a href="#">Home</a>
    <a href="#">Remedy Type ▾</a>
    <a class="active" href="#">Health Condition ▾</a>
    <a href="#">Accessories &amp; Supplies ▾</a>
    <a href="#">Loyalty Program</a>
    <a href="#">Contact us</a>
  </nav>
</header>

<section>
  <div class="abs hero-photo" role="img" aria-label="Photo of a carer holding the hands of an elderly person gripping a small ball"></div>
  <div class="abs hero-shade"></div>
  <h1 class="abs hero-title">Health Condition</h1>
  <p class="abs hero-text">We have the best doctors, Herbalist, Aromatherapist and Health Professional that are ready to offers consultation and helping others with their vast insights In their fields..</p>
</section>

<aside>
  <h2 class="abs side-title">Health Condition</h2>
  <ul class="abs side-list">
    <li>Allergies</li><li>Cardiovascular</li><li>Children's Health</li><li class="on">Cleansing</li><li>Immune</li><li>Infections</li><li>Joints &amp; Muscles</li><li>Men's Health</li><li>Women's Health</li><li>Nasal &amp; Respiratory</li><li>Nervous System</li><li>Pregnancy &amp; Postnatal</li><li>Skin</li><li>Stress &amp; Tension</li><li>Urinary</li><li>Anti Inflammatory</li><li>Blood Sugar</li><li>Calming and Sleep</li><li>Circulation</li><li>Cold, Flu and Fever</li><li>Digestion</li><li>Fungal Infections</li><li>Liver support</li><li>Memory</li><li>Oral Health</li><li>Parasites</li><li>Thyroid Gland</li><li>Vein health</li><li>Virus</li>
  </ul>
</aside>

<main>
  <div class="abs toolbar" style="left:419px"><b>12</b> PRODUCTS FOUND</div>
  <div class="abs toolbar" style="left:622px">SORT BY: &nbsp;DEFAULT &nbsp;▾</div>
  <div class="abs toolbar" style="left:814px">SHOW: &nbsp;9 &nbsp;▾</div>
  <div class="abs toolbar" style="left:944px">VIEW</div>
  <svg class="abs" style="left:987px;top:760px" width="16" height="16" viewBox="0 0 16 16" fill="#4a7c0c">
    <rect x="0" y="0" width="4" height="4"/><rect x="6" y="0" width="4" height="4"/><rect x="12" y="0" width="4" height="4"/>
    <rect x="0" y="6" width="4" height="4"/><rect x="6" y="6" width="4" height="4"/><rect x="12" y="6" width="4" height="4"/>
    <rect x="0" y="12" width="4" height="4"/><rect x="6" y="12" width="4" height="4"/><rect x="12" y="12" width="4" height="4"/>
  </svg>
  <svg class="abs" style="left:1017px;top:761px" width="19" height="14" viewBox="0 0 19 14" fill="#ccc">
    <rect x="0" y="0" width="3" height="2"/><rect x="5" y="0" width="14" height="2"/>
    <rect x="0" y="6" width="3" height="2"/><rect x="5" y="6" width="14" height="2"/>
    <rect x="0" y="12" width="3" height="2"/><rect x="5" y="12" width="14" height="2"/>
  </svg>

  <article class="abs card sel" style="left:419px;top:808px">
    <div class="thumb" role="img" aria-label="Amber dropper bottle of tincture"></div>
    <h3 class="name">Agrimony</h3><p class="desc">Extract (Tincture)<br>(Agrimonia Eupatoria)</p>
  </article>
  <article class="abs card" style="left:644px;top:808px">
    <div class="thumb" role="img" aria-label="Amber dropper bottle of tincture"></div>
    <h3 class="name">Alfalfa Tincture</h3><p class="desc">(Medicago Sativa)</p>
  </article>
  <article class="abs card" style="left:868px;top:808px">
    <div class="thumb" role="img" aria-label="Amber dropper bottle of tincture"></div>
    <h3 class="name">Damiana</h3><p class="desc">Extract (Tincture)<br>(Turnera diffusa)</p>
  </article>

  <article class="abs card" style="left:419px;top:1118px">
    <div class="thumb" role="img" aria-label="Amber dropper bottle of tincture"></div>
    <h3 class="name">Chasteberry / Vitex</h3><p class="desc">Extract (Tincture) (Vitex agnus-castus )</p>
  </article>
  <svg class="abs star" width="28" height="28" viewBox="0 0 28 28"><polygon points="14,1 17.5,9.5 27,10 19.6,16 22,25.5 14,20.3 6,25.5 8.4,16 1,10 10.5,9.5" fill="#f2b01e"/><text x="14" y="18" font-family="Open Sans,sans-serif" font-size="10" font-weight="700" fill="#fff" text-anchor="middle">5</text></svg>
  <article class="abs card" style="left:644px;top:1118px">
    <div class="thumb photo-a" role="img" aria-label="Photo of a herbal tea blend in a cup"></div>
    <h3 class="name">After Dinner</h3>
  </article>
  <article class="abs card" style="left:868px;top:1118px">
    <div class="thumb photo-b" role="img" aria-label="Photo of herb sachets in a wicker basket"></div>
    <h3 class="name">Allerease</h3>
  </article>

  <article class="abs card" style="left:419px;top:1442px">
    <div class="thumb" role="img" aria-label="Amber dropper bottle of tincture"></div>
    <h3 class="name">Alterative</h3><p class="desc">Formulation (Extract)</p>
  </article>
  <article class="abs card" style="left:644px;top:1442px">
    <div class="thumb" role="img" aria-label="Amber dropper bottle of tincture"></div>
    <h3 class="name">Anti-Diarrhoea</h3><p class="desc">Formulation<br>(Extract)</p>
  </article>
  <article class="abs card" style="left:868px;top:1442px">
    <div class="thumb" role="img" aria-label="Amber dropper bottle of tincture"></div>
    <h3 class="name">Angelica</h3><p class="desc">Extract (Tincture)<br>(Angelica Archangelica)</p>
  </article>

  <nav class="abs pager"><span class="cur">1</span><span>2</span><span>3</span><span>4</span><span>5</span><span>6</span><span>7</span><span class="next">NEXT</span></nav>
</main>

<footer>
  <div class="abs footer-band"></div>
  <a class="brand footer-brand" href="#"><span class="brand-dot"></span><span>Fernmoor Well</span></a>
  <p class="abs mission">Fernmoor Well's mission is to provide our clients with exceptional plant based Health Care products to purify and uplift the body and spirit.</p>
  <p class="abs contact">Tel: <span>555.014.2290</span><br>Fax: <span>555.014.2291</span><br>Email: <span>info@fernmoorwell.com</span></p>
  <div class="abs fcol" style="left:536px"><h4>MAIN LINKS</h4>Home<br>Remedy Type<br>Health Conditions<br>Loyalty Program<br>About Us<br>Contact us</div>
  <div class="abs fcol" style="left:723px"><h4>INFORMATION</h4>Shipping Information<br>Consultation<br>Community Links<br>Health Info<br>Returns Policy<br>Returns</div>
  <div class="abs fcol" style="left:911px"><h4>MY ACCOUNT</h4>My Account<br>Order History<br>Newsletter<h4 style="margin-top:14px">EXTRAS</h4>Brands<br>Gift Vouchers<br>Specials</div>
  <a class="abs totop" href="#"><svg width="8" height="6" viewBox="0 0 8 6"><path d="M1 5 4 2 7 5" fill="none" stroke="#555" stroke-width="1.3"/></svg></a>
  <div class="abs bottombar"><span class="l">Fernmoor Well Herbal Dispensary © 2017</span><span class="r">Privacy Policy - Terms &amp; Conditions - Site Map</span></div>
</footer>

</body>
</html>
```